Four Quiet Steps Toward a Stronger Offer on THE Property - VARN Real Estate

I have written an E-Book that is called "Four Quiet Steps Toward a Stronger Offer on The Property." The E-Book will be available as a FREE download from my VARN Real Estate landing page, and also from a Chatterbox campaign that will be commencing in early September.

The E-Book content is in the WORD document below - I now need for it to be made to look more professional and suitable for publishing and placed on my landing page for download. Please review and send me some proposals for this e-book to be a bit more eye catching and appealing than just a WORD doc.

My VARN Real Estate landing page is still under development and you can see the what is close to the final proposal here:

http://www.plum-orbit.com.au/varn/

The cover of the E-Book is at the bottom of the page. Please review and give the internals the sale look and feel.

Target Market(s)

Home and Property Owners in the middle ring Eastern Suburbs of Melbourne - approximately 15 - 30 km's from the central business district. The area is a very family oriented area and features mostly houses that are 3 or 4 bedroom - with some larger properties that are five or more bedrooms. The area is quite an expensive suburban community and house prices range between the low of $1,000,000 to a high of more than $2,500,000. The predominant cultural group that buys in this area are Chinese and Chinese Australian buyers. The predominant group who are selling are usually Australians of a white anglo-saxon background. Other groups are of Asian sub continent background (Indian / Sri Lankan/ Pakistan). All are families that are attracted to the area because of the great schools, good shopping, leisure facilities (parks, pools, courts etc), and excellent public and road transport infrastructure. Read the content of my e-book - it tells you every thing you need to know :)

Industry/Entity Type

Real Estate

Colors

Designer to choose colors to be used in the design.

Requirements
Must have
• Once completed the layout should not be too busy - it should be easy to read. I guess then the statement "less is more" is applicable.
• I will probably print a number of copies of this book for distribution as well - so please consider print attributes in the design.
• IMPORTANT: as for any e-book offering specialist advice, the MAIN reason for the book is for the generation of sales leads and to establish the author as a subject matter expert on the topic. Please consider this in your design elements. BUT - the book should also not come across as 1 big advertisement either. Subtle but impactful are well chosen words to describe how it should present.
Nice to have
• VARN Real Estate branding on every page - to re-inforce the message.
Should not have
• No need for animations or illustrations/

```html
<!DOCTYPE html>
<html lang="en">
<head>
<meta charset="utf-8">
<title>Four Quiet Steps Toward a Stronger Offer on The Property – VARN Real Estate</title>
<link href="https://fonts.googleapis.com/css2?family=Montserrat:wght@400;500;600;700;800&family=Questrial&family=Lora:ital@1&display=swap" rel="stylesheet">
<style>
:root{
  --stage-light:#a4a4a4;
  --stage-dark:#4e4e4e;
  --ink:#1f1f1f;
  --text:#565656;
  --muted:#8d8d8d;
  --band:#232323;
  --paper-edge:#d6d6d6;
  --paper-mid:#f5f5f5;
  --silver-hi:#fbfbfb;
  --silver-lo:#8f8f8f;
  --white:#ffffff;
  --tick:#7a7a7a;
}
*{box-sizing:border-box;margin:0;padding:0}
html,body{width:893px;height:1200px;overflow:hidden}
body{
  position:relative;
  background:radial-gradient(ellipse at 50% 45%,var(--stage-light) 0%,#7d7d7d 55%,var(--stage-dark) 100%);
  font-family:'Questrial',sans-serif;
}
.label{
  position:absolute;width:384px;text-align:center;
  font-family:'Montserrat',sans-serif;font-weight:700;font-size:18px;
  color:var(--white);letter-spacing:1px;
}
.page{position:absolute;width:384px;height:544px;overflow:hidden;box-shadow:0 2px 10px rgba(0,0,0,.35)}
.col-left{left:55px}.col-right{left:454px}
.row-top{top:50px}.row-bottom{top:610px}

/* cover */
.cover{background:linear-gradient(to bottom,#121212 0%,#2b2b2b 30%,#3b3b3b 50%)}
.cover-brand{position:absolute;top:30px;width:100%;text-align:center;color:var(--white)}
.cover-brand .name{font-family:'Montserrat',sans-serif;font-weight:500;font-size:44px;letter-spacing:2px;line-height:1}
.cover-brand .sub{font-family:'Montserrat',sans-serif;font-size:8px;letter-spacing:8.5px;margin-top:4px;padding-left:8px}
.cover-rings{position:absolute;left:0;top:0}
.cover-photo{position:absolute;left:0;top:270px;width:384px;height:240px;
  background:linear-gradient(to bottom,#9fb1c0 0%,#6f8766 22%,#4f8a2c 45%,#3f7a22 75%,#2f5d1a 100%)}
.cover-title{position:absolute;left:81px;top:154px;width:224px;height:224px;border-radius:50%;
  background:radial-gradient(circle at 45% 35%,var(--silver-hi) 0%,#d8d8d8 45%,var(--silver-lo) 100%);
  box-shadow:0 0 0 4px #6a6a6a,0 4px 12px rgba(0,0,0,.5);
  display:flex;flex-direction:column;align-items:center;justify-content:center;
  font-family:'Montserrat',sans-serif;color:#2a2a2a;text-align:center;line-height:1}
.cover-title .big{font-weight:800;font-size:27px;letter-spacing:.5px}
.cover-title .huge{font-weight:800;font-size:33px}
.cover-title .mid{font-weight:500;font-size:14px;margin:3px 0}
.cover-title .bold-mid{font-weight:800;font-size:22px}
.cover-number{position:absolute;left:151px;top:104px;width:84px;height:84px;border-radius:50%;
  background:radial-gradient(circle at 45% 35%,var(--silver-hi) 0%,#cfcfcf 50%,#7d7d7d 100%);
  box-shadow:0 0 0 3px #555,0 3px 8px rgba(0,0,0,.5);
  display:flex;align-items:center;justify-content:center;
  font-family:'Montserrat',sans-serif;font-weight:800;font-size:54px;color:#222}
.cover-url{position:absolute;left:0;bottom:0;width:100%;height:34px;background:#151515;
  color:var(--white);font-family:'Montserrat',sans-serif;font-size:10px;text-align:center;line-height:34px}

/* inner pages */
.inner{background:linear-gradient(to right,var(--paper-edge) 0%,var(--paper-mid) 50%,#dddddd 100%)}
.running-head{position:absolute;left:0;top:0;width:100%;height:32px;background:linear-gradient(to bottom,#1a1a1a,var(--band))}
.running-head .title{position:absolute;left:16px;top:12px;font-family:'Montserrat',sans-serif;font-size:6.6px;color:var(--muted);letter-spacing:.2px}
.brand-tab{position:absolute;right:16px;top:0}
.content{position:absolute;left:16px;right:16px;top:46px;bottom:34px;overflow:hidden;color:var(--text);font-size:6.9px;line-height:9.2px;text-align:justify}
.content p{margin-bottom:6px}
.content b{color:#333}
h2.section{font-family:'Montserrat',sans-serif;font-weight:700;font-size:9px;color:var(--ink);margin:6px 0 5px;letter-spacing:.2px}
h2.feature{font-family:'Montserrat',sans-serif;font-weight:700;font-size:12.5px;color:var(--ink);margin:8px 0 6px;display:flex;align-items:center;gap:6px;letter-spacing:.3px}
h3.lead{font-family:'Montserrat',sans-serif;font-weight:700;font-size:9px;color:var(--ink);margin:6px 0 4px}
h4.list-head{font-family:'Montserrat',sans-serif;font-weight:700;font-size:6.9px;color:var(--ink);margin:8px 0 4px}
.checks{list-style:none}
.checks li{position:relative;padding-left:15px;margin-bottom:8px}
.checks.tight li{margin-bottom:5px}
.checks li::before{content:"";position:absolute;left:0;top:0;width:9px;height:9px;border-radius:50%;background:var(--tick)}
.checks li::after{content:"";position:absolute;left:3.2px;top:1.6px;width:2.4px;height:4.3px;border:solid var(--white);border-width:0 1.3px 1.3px 0;transform:rotate(45deg)}
.quote{background:var(--band);color:#eee;font-family:'Lora',serif;font-style:italic;font-size:7.3px;line-height:10px;padding:8px 12px;margin:10px 0 12px;text-align:left}
.folio{position:absolute;left:8px;right:8px;bottom:22px;height:1px;background:#3a3a3a}
.folio span{position:absolute;left:50%;top:-8px;margin-left:-9px;width:18px;height:18px;background:#151515;border-radius:50%;
  color:var(--white);font-family:'Montserrat',sans-serif;font-size:6px;font-weight:700;text-align:center;line-height:18px}
</style>
</head>
<body>

<div class="label col-left" style="top:18px">FRONT PAGE</div>
<div class="label col-right" style="top:18px">INNER PAGE 1</div>
<div class="label col-left" style="top:1164px">INNER PAGE 2</div>
<div class="label col-right" style="top:1164px">INNER PAGE 3</div>

<!-- Cover -->
<section class="page cover col-left row-top">
  <div class="cover-photo" role="img" aria-label="Aerial photo of a white family house on green rolling lawns with a pond and trees"></div>
  <svg class="cover-rings" width="384" height="544" viewBox="0 0 384 544" aria-hidden="true">
    <circle cx="193" cy="266" r="150" fill="none" stroke="#666" stroke-width=".6"/>
    <circle cx="193" cy="266" r="175" fill="none" stroke="#555" stroke-width=".5"/>
    <circle cx="193" cy="146" r="58" fill="none" stroke="#777" stroke-width=".6"/>
    <line x1="0" y1="146" x2="384" y2="146" stroke="#555" stroke-width=".4"/>
    <line x1="193" y1="80" x2="193" y2="270" stroke="#555" stroke-width=".4"/>
  </svg>
  <div class="cover-brand">
    <div class="name">VARN</div>
    <div class="sub">REAL ESTATE</div>
  </div>
  <div class="cover-title">
    <div class="big" style="margin-top:14px">FOUR QUIET</div>
    <div class="huge">STEPS</div>
    <div class="mid">TOWARD A STRONGER</div>
    <div class="bold-mid">OFFER ON</div>
    <div class="mid">THE PROPERTY</div>
  </div>
  <div class="cover-number">4</div>
  <div class="cover-url">www.plum-orbit.com.au/varn/</div>
</section>

<!-- Inner page 1 -->
<section class="page inner col-right row-top">
  <header class="running-head">
    <div class="title">FOUR QUIET STEPS TOWARD A STRONGER OFFER ON THE PROPERTY</div>
    <svg class="brand-tab" width="62" height="46" viewBox="0 0 62 46">
      <defs><linearGradient id="tab1" x1="0" y1="0" x2="0" y2="1"><stop offset="0" stop-color="#f4f4f4"/><stop offset="1" stop-color="#a9a9a9"/></linearGradient></defs>
      <polygon points="0,0 62,0 62,46 31,38 0,46" fill="url(#tab1)"/>
      <text x="31" y="26" text-anchor="middle" font-family="Montserrat,sans-serif" font-weight="600" font-size="17" fill="#222">VARN</text>
    </svg>
  </header>
  <div class="content">
    <h2 class="section">CITY OF ASHVALE &amp; CITY OF KERROW</h2>
    <p>So after much consideration you have made the decision to sell your property. For some of you the home may have held many long and happy memories. For others it may have been a property used purely as an investment vehicle to greater wealth. Unfortunately for some others it may be necessary to sell due to life challenges – these may be financial issues, a marriage breakdown or even the passing away of a relative. Whatever the reason and your motivation for selling – once the decision to sell is made, the most important end result is to get for your property the best possible price available in the market place.</p>
    <p>In my free e-book – you will find <b>Four Quiet Steps Toward a Stronger Offer on The Property</b>. It includes some useful tips to help you prepare your property to be put on the market for sale. Then once it is ready – what to do to extract top dollar for the sale of your home.</p>
    <h2 class="section" style="margin-top:10px">BY THE WAY....CONGRATULATIONS ON YOUR CHOICE OF LOCATION</h2>
    <p>The desirable and leafy City of Ashvale and City of Kerrow are exceptionally popular residential locations – and it is little wonder when you consider all that they offer to the modern family. The standout features of these two great municipalities include:</p>
    <ul class="checks" style="margin-top:10px">
      <li><b>Superb education options</b> - some of Melbourne's leading government and private primary and secondary schools are located within the boundaries of the City of Ashvale and the City of Kerrow. There are also excellent tertiary education choices present with Corran University (Linden campus), Ashvale University (Marlow campus), Fernleigh Institute, and the State Police Academy, amongst others all located in the region. And the range of great childcare and Kindergarten options round out an amazing list of K-12 education options and beyond for local residents.</li>
      <li><b>Outstanding shopping</b> exists and includes shopping centres like Glenmoor Plaza, Hillcrest Village, Cedarway Village, Bramley Park, Oakfield Chase, Ridgeview Central as well as a number of smaller strip shopping and local centres.</li>
      <li><b>Beautiful parks, gardens, trails and outdoor leisure facilities</b> including Pellam Park, Brook Reserve, Larkmoor Lake Sanctuary, Ferrier's Creek Linear Trail, Hollowdale Golf Club, Elmsdale Golf Course, Glen Marrow Public Golf Course and many other sporting facilities and grounds.</li>
      <li><b>A large number of public transport</b> choices for commuters and students spread right across the region including trains, trams and buses depending on your location.</li>
      <li><b>Excellent freeway and road infrastructure</b> that is continuously evolving and includes the Ashvale Freeway, Eastway Link, and the Ridge Freeway. All parts of Melbourne are easily accessible from the City of Ashvale and the City of Kerrow.</li>
    </ul>
    <p style="margin-top:10px">Education, shopping convenience, leisure facilities and transport infrastructure form the back bone of any desirable community – and the attraction of families, investors and developers to these popular and well established residential areas ensure that the foundation for interest in your property is already in place. So in order for your home to sell well and achieve the best possible price, here are the <b>Four Quiet Steps Toward a Stronger Offer on The Property</b> to help you on your journey.</p>
  </div>
  <div class="folio"><span>01</span></div>
</section>

<!-- Inner page 2 -->
<section class="page inner col-left row-bottom">
  <header class="running-head">
    <div class="title">FOUR QUIET STEPS TOWARD A STRONGER OFFER ON THE PROPERTY</div>
    <svg class="brand-tab" width="62" height="46" viewBox="0 0 62 46">
      <defs><linearGradient id="tab2" x1="0" y1="0" x2="0" y2="1"><stop offset="0" stop-color="#f4f4f4"/><stop offset="1" stop-color="#a9a9a9"/></linearGradient></defs>
      <polygon points="0,0 62,0 62,46 31,38 0,46" fill="url(#tab2)"/>
      <text x="31" y="26" text-anchor="middle" font-family="Montserrat,sans-serif" font-weight="600" font-size="17" fill="#222">VARN</text>
    </svg>
  </header>
  <div class="content">
    <h2 class="section">PROPERTY PRESENTATION</h2>
    <p>Like any product – the newer, the cleaner, the shinier, and the better presented a property is for sale...then the more interest it will attract from prospective Buyers.</p>
    <p>The more Buyer interest that a property attracts...the more competition around the purchase price that will be created.</p>
    <p>And Buyer competition is fantastic if you know how to harness it to achieve the best possible sale price. But where is it that you should begin and how?</p>
    <p>So let's start at the very beginning – property preparation and presentation for sale.</p>
    <p>It is important to state that very few people actually live in the manner that a house is presented for sale. In most instances what you see at homes that are open for Buyer inspection is the end result of a lot of hard work on behalf of the Vendor and others.</p>
    <p>So don't be concerned – however and whatever your home looks like now...it can be transformed to maximize its appeal to Buyers.</p>
    <div class="quote">“Vendor's will always see all of the great and wonderful aspects of their property in an effort to create value and push up the price; a Buyer will always tell you everything that is wrong in an effort to drive down the price.”</div>
    <p>The whole process of buying and selling property is very psychological and highly emotional for most people, so it is very important for Vendors to place themselves in the shoes of a Buyer when running a critical eye across the presentation preparations.</p>
    <p>Your property should be polished, displayed and presented to the highest possible standard. That standard will be different for everyone – factoring in age, ability, financial capacity, the size of family, number of pets and so on.</p>
    <p>In addition - every property is different, and every property has it's own features and personality – what's important is to amplify the positives and minimize the impact of the negatives throughout the home.</p>
    <h3 class="lead">Let's look at some of the basics:</h3>
    <h2 class="feature">
      <svg width="14" height="13" viewBox="0 0 14 13" aria-hidden="true"><path d="M7 0 L14 6 L12 6 L12 13 L8.5 13 L8.5 9 L5.5 9 L5.5 13 L2 13 L2 6 L0 6 Z" fill="#1f1f1f"/></svg>
      CURBSIDE APPEAL</h2>
    <p>First impressions count - stand outside at the front of your house on the street and look at your house with a critical eye. Does your home stand out as a welcoming and “happy” place to arrive at?</p>
    <p>Tidy the gardens, mow the lawns, repair the gutters, paint under the eaves of the roof, clean the windows, repair the cracks in the cement driveways and do some basic landscaping such as adding mulch to garden beds (my personal preference for mulch is black tan bark – but other varieties are just as effective). You will find all these tasks make a huge difference to the exterior look and feel of your property.</p>
    <p>If your property has a fence, then clean it and paint it. Cut back any overgrown trees and bushes, trim and shape the edges of pathways, and clear and remove all rubbish (including rubbish bins) from the front of the house.</p>
  </div>
  <div class="folio"><span>02</span></div>
</section>

<!-- Inner page 3 -->
<section class="page inner col-right row-bottom">
  <header class="running-head">
    <div class="title">FOUR QUIET STEPS TOWARD A STRONGER OFFER ON THE PROPERTY</div>
    <svg class="brand-tab" width="62" height="46" viewBox="0 0 62 46">
      <defs><linearGradient id="tab3" x1="0" y1="0" x2="0" y2="1"><stop offset="0" stop-color="#f4f4f4"/><stop offset="1" stop-color="#a9a9a9"/></linearGradient></defs>
      <polygon points="0,0 62,0 62,46 31,38 0,46" fill="url(#tab3)"/>
      <text x="31" y="26" text-anchor="middle" font-family="Montserrat,sans-serif" font-weight="600" font-size="17" fill="#222">VARN</text>
    </svg>
  </header>
  <div class="content">
    <p>By improving your properties curbside appeal and street presence you will not only allow Buyers to have an immediate positive first impression – you are also ensuring that the property is ready to be photographed for the all important exterior façade shot as part of the marketing and advertising.</p>
    <h2 class="feature">
      <svg width="10" height="14" viewBox="0 0 10 14" aria-hidden="true"><rect x="3.5" y="0" width="3" height="6" fill="#1f1f1f"/><rect x="1" y="6" width="8" height="2" fill="#1f1f1f"/><path d="M1 8 L9 8 L9 14 L1 14 Z" fill="#1f1f1f"/></svg>
      CLEANING AND DE-CLUTTERING</h2>
    <p>If you have been living in your home for anymore than a few years, then you might be surprised at the amount of “things” that you have accumulated. Most people do not genuinely live in the manner that they present a property when they sell. And less is definitely more when it comes to the sale of your home and the reduction of “things” in the home.</p>
    <p>Our friends at <b>www.tidyhomeplan.com.au</b> offer the following tips when it comes to de-cluttering:</p>
    <h4 class="list-head">Top Tips on How to De-clutter your Home</h4>
    <ul class="checks tight">
      <li>Just start. Don't overthink it; just start getting rid of things!</li>
      <li>Deal with rubbish first. Start by going through each room with a big garbage bag and throwing away anything that isn't saleable or suitable for charity.</li>
      <li>De-clutter by category not by room. It is less overwhelming to de-clutter by category (such as clearing out DVD's or linen) than to tackle a whole room.</li>
      <li>It's about progress not perfection. Don't be discouraged, clutter takes time to build up and it will take time to deal with.</li>
      <li>If you don't need it, why not donate it or throw it away?</li>
      <li>Remove all books from bookcases.</li>
      <li>Pack up those knickknacks.</li>
      <li>Clean off everything on kitchen counters.</li>
      <li>Put essential items used daily in a small box that can be stored in a closet when not in use.</li>
      <li>Think of this process as a head start on the packing you will eventually need to do anyway.</li>
    </ul>
    <p style="margin-top:8px">Of equal importance is the organization and arrangement of the areas that cannot be immediately seen. Cupboards, closets, linen presses and pantries inside the property. Buyers WILL open and look inside pantries, cupboards and wardrobes – so the more organized they are the better impression a Buyer will have of the property.</p>
    <p>If you have a lot of packing boxes and surplus furniture to be removed and put away, and an off-site storage space is not an option...then a garage on the property can be used so long as items are neatly packed and safely stored.</p>
    <h2 class="feature">
      <svg width="13" height="13" viewBox="0 0 13 13" aria-hidden="true"><path d="M1 12 L7 6" stroke="#1f1f1f" stroke-width="2.4" stroke-linecap="round"/><circle cx="9" cy="4" r="3.4" fill="#1f1f1f"/><circle cx="10.3" cy="2.7" r="1.4" fill="#ececec"/></svg>
      MAINTENANCE &amp; PAINTING</h2>
    <p>Walk through your property and check that all lights are working (replace the globes if they are not working); identify and fill any cracks in the walls, floor and ceiling; apply a coat or two of paint externally and internally.</p>
  </div>
  <div class="folio"><span>03</span></div>
</section>

</body>
</html>
```